Stock Window Screen Designs for a Mobile App

Come up with new modern mobile screen designs for a Stock Window feature.

*The existing desktop version of this feature consists of (4) pages. The new mobile design does not necessarily need to use tabs for navigation. Accordions or some other new modern method of navigation between the pages may also be considered.

*Please include both Light and Dark Theme versions

*** Update ****
The 4th Tab Page [Similar to ...] is shown with solid row colors. These indicate the buy/sell volume direction. For the new mobile design it is ok to use a small icon with the color instead of solid row colors. Or some other innovative way to show the same.

Target Market(s)

Day Traders

Requirements
Must have
• Light and Dark Theme Versions

```html
<!DOCTYPE html>
<html lang="en">
<head>
<meta charset="utf-8">
<title>Stock Window – Mobile Screens</title>
<link href="https://fonts.googleapis.com/css2?family=Montserrat:wght@400;500;600;700&display=swap" rel="stylesheet">
<style>
:root{
  --brand:#05659b;
  --page:#ffffff;
  --up:#1fb34a;
  --down:#e32626;
}
.theme-light{
  --header:#05659b; --surface:#ffffff; --card:#f4f5f6; --text:#2f3338;
  --muted:#8a8f95; --accent:#05659b; --nav:#05659b; --line:#e3e5e8;
  --input:#ffffff; --input-text:#2f3338; --icon:#05659b;
}
.theme-dark{
  --header:#000000; --surface:#262626; --card:#3a3a3a; --text:#f1f1f1;
  --muted:#9a9a9a; --accent:#ffffff; --nav:#000000; --line:#4a4a4a;
  --input:#3a3a3a; --input-text:#ffffff; --icon:#e8e8e8;
}
*{box-sizing:border-box;margin:0;padding:0}
html,body{width:749px;height:1200px;overflow:hidden;background:var(--page)}
body{font-family:'Montserrat',sans-serif}
.board{position:absolute;left:0;top:0;width:1498px;height:2400px;transform:scale(.5);transform-origin:0 0}
.board-heading{position:absolute;font-size:15.5px;font-weight:600;color:var(--brand);letter-spacing:.2px;white-space:nowrap}

.screen{position:absolute;width:200px;border-radius:10px;overflow:hidden;display:flex;flex-direction:column;background:var(--header)}
.status{height:22px;flex:none;display:flex;justify-content:space-between;align-items:center;padding:0 8px;font-size:5.5px;color:#fff;font-weight:500}
.status-icons{display:flex;gap:3px;align-items:center}
.status-icons span{display:block;background:#fff;opacity:.85}
.sig{width:6px;height:4px;clip-path:polygon(0 100%,100% 0,100% 100%)}
.wifi{width:5px;height:4px;border-radius:3px 3px 0 0}
.batt{width:9px;height:4px;border-radius:1px}
.title{flex:none;text-align:center;font-size:12.5px;font-weight:600;color:#fff;padding:7px 0 16px;line-height:15px;white-space:nowrap}
.content{flex:1;background:var(--surface);border-radius:18px 18px 0 0;overflow:hidden}
.nav{flex:none;height:44px;background:var(--nav);display:flex;justify-content:space-around;align-items:center;padding:0 8px}
.nav-item{position:relative;display:flex;flex-direction:column;align-items:center;gap:3px;font-size:4.6px;color:rgba(255,255,255,.55);height:44px;justify-content:center;width:40px}
.nav-item svg{width:11px;height:11px;fill:none;stroke:rgba(255,255,255,.75);stroke-width:1.2}
.nav-item.is-active{color:#fff}
.nav-item.is-active svg{stroke:#fff}
.nav-item.is-active::after{content:"";position:absolute;bottom:0;width:20px;height:3px;border-radius:2px 2px 0 0;background:#fff}

.ico{width:16px;height:16px;fill:none;stroke:var(--icon);stroke-width:1}

/* Details */
.picker{margin:4px 8px 0;height:28px;background:var(--input);display:flex;align-items:center;justify-content:space-between;padding:0 14px;font-size:9px;font-weight:500;color:var(--input-text)}
.chev{width:8px;height:5px;fill:none;stroke:currentColor;stroke-width:1;opacity:.6}
.company{display:flex;align-items:center;gap:9px;padding:12px 10px 9px;font-size:7px;color:#fff;font-weight:500;line-height:11px;white-space:nowrap}
.company-mark{width:19px;height:11px;background:#c9d3df;flex:none}
.quote{display:flex;align-items:center;padding:16px 0 10px 22px;height:85px}
.brand-word{width:78px;font-size:16px;font-weight:700;color:#1877f2}
.price{font-size:13.5px;font-weight:600;color:var(--text)}
.quote-time{display:flex;align-items:center;gap:4px;font-size:7px;color:var(--muted);margin-top:5px;white-space:nowrap}
.quote-time .ico{width:11px;height:11px}
.change{font-size:7px;color:var(--down);margin-top:5px}
.volume-box{margin:0 8px;height:52px;background:var(--card);display:flex;align-items:center;padding:0 12px;border-radius:2px}
.volume-col{flex:1;font-size:7px;color:var(--muted)}
.volume-col + .volume-col{border-left:1px solid var(--line);padding-left:16px}
.volume-col strong{display:block;color:var(--text);font-size:8px;font-weight:600;margin-top:6px}
.metric{margin:5px 8px 0;height:38px;background:var(--card);display:grid;grid-template-columns:20px 98px 1fr;align-items:center;padding:0 10px;border-radius:2px}
.metric-label{font-size:7px;color:var(--text);padding-left:8px;opacity:.85;white-space:nowrap}
.metric-value{font-size:8px;font-weight:700;color:var(--text);white-space:nowrap}
.metric-value sup{font-size:5px;margin-right:2px}
.metric-value small{display:block;font-size:4.5px;font-weight:500;color:var(--muted)}
.metric-value.is-down{color:var(--down)}
.tri{color:var(--up);font-size:6px;margin-right:4px}

/* News */
.news-list{padding:0 20px}
.news-item{height:117px;padding-top:20px;border-bottom:1px solid var(--line)}
.news-date{display:flex;align-items:center;gap:6px;font-size:6.5px;color:var(--muted)}
.news-date .ico{width:12px;height:12px}
.news-headline{font-size:8px;color:var(--text);line-height:14.5px;margin-top:9px}
.news-source{font-size:6.5px;color:var(--muted);margin-top:8px}

/* Profile */
.profile-body{padding:8px}
.profile-card{height:98px;background:var(--card);border-radius:6px;padding:18px 14px;margin-bottom:8px}
.profile-card-head{display:flex;align-items:center;gap:8px;font-size:9px;font-weight:500;color:var(--accent)}
.profile-card-head .ico{width:22px;height:22px}
.profile-card p{font-size:8px;color:var(--muted);line-height:17px;margin-top:6px;padding-left:4px}
.section-label{font-size:8px;font-weight:600;color:var(--text);margin:20px 2px 10px}
.summary{background:var(--card);border-radius:6px;padding:12px 16px;font-size:7.4px;color:var(--muted);line-height:16.6px}

/* Similar */
.select-label{text-align:center;font-size:7.5px;font-weight:500;color:var(--accent);margin-top:16px}
.search{margin:10px 8px 0;height:28px;border:1px solid var(--line);background:var(--surface);display:flex;align-items:center;gap:6px;padding:0 8px;font-size:7px;color:var(--muted)}
.theme-dark .search{border-color:#8a8a8a;color:#eee}
.search svg{width:9px;height:9px;fill:none;stroke:currentColor;stroke-width:1.4}
.symbol-panel{margin:14px 8px 0;background:var(--card);padding-bottom:14px}
.symbol-row{margin:6px 8px 0;height:38px;background:var(--card);display:flex;align-items:center;justify-content:space-between;padding:0 14px;font-size:7.5px;font-weight:500;color:var(--text)}
.symbol-panel .symbol-row{margin:0;height:36px}
.symbol-panel .chev{opacity:1}
.stat{display:flex;justify-content:space-between;padding:0 18px;height:36px;align-items:center;font-size:7px;color:var(--text);white-space:nowrap}
.stat strong{font-size:7.5px;font-weight:700}
.company-name{padding:6px 18px 0;font-size:7px;color:var(--text)}
.company-name strong{display:block;font-size:8px;font-weight:700;margin-top:10px;white-space:nowrap}
</style>
</head>
<body>
<div class="board">

  <h2 class="board-heading" style="left:153px;top:79px">01. Details Screen</h2>
  <h2 class="board-heading" style="left:475px;top:79px">02. News</h2>
  <h2 class="board-heading" style="left:807px;top:74px">03. Profile</h2>
  <h2 class="board-heading" style="left:1128px;top:70px">04. Similar to NOVA</h2>

  <h2 class="board-heading" style="left:153px;top:1199px">01. Details Screen</h2>
  <h2 class="board-heading" style="left:475px;top:1199px">02. News</h2>
  <h2 class="board-heading" style="left:807px;top:1194px">03. Profile</h2>
  <h2 class="board-heading" style="left:1128px;top:1189px">04. Similar to NOVA</h2>

  <!-- LIGHT: DETAILS -->
  <section class="screen theme-light" style="left:160px;top:132px;height:909px">
    <div class="status"><span>11.58 am</span><span class="status-icons"><span class="sig"></span><span class="wifi"></span><span class="batt"></span></span></div>
    <div class="title">Details</div>
    <div class="picker">NOVA <svg class="chev" viewBox="0 0 8 5"><path d="M.5.5 4 4 7.5.5"/></svg></div>
    <div class="company"><span class="company-mark"></span>Nova Platforms, Inc. (NXE:NOVA)</div>
    <div class="content">
      <div class="quote">
        <div class="brand-word">NOVA</div>
        <div>
          <div class="price">176.99</div>
          <div class="quote-time"><svg class="ico" viewBox="0 0 16 16"><rect x="2" y="3" width="12" height="11" rx="1"/><path d="M2 6h12M5 1.5v3M11 1.5v3"/></svg>2.53 PM 8/11/2022</div>
          <div class="change">-1.35 (-0.76%)</div>
        </div>
      </div>
      <div class="volume-box">
        <div class="volume-col">Volume<strong>19,012,888</strong></div>
        <div class="volume-col">Relative Volume<strong>0.92</strong></div>
      </div>
      <div class="metric"><svg class="ico" viewBox="0 0 16 16"><path d="M2 9v-3M5 12V4M8 14V2M11 11V5M14 9V7"/></svg><span class="metric-label">Float</span><span class="metric-value">2.28B</span></div>
      <div class="metric"><svg class="ico" viewBox="0 0 16 16"><rect x="2" y="3" width="12" height="11" rx="1"/><path d="M2 6h12M5 1.5v3M11 1.5v3"/><circle cx="11" cy="11" r="2.5"/></svg><span class="metric-label">Earnings Date</span><span class="metric-value">July 27<small>POST.MKT</small></span></div>
      <div class="metric"><svg class="ico" viewBox="0 0 16 16"><path d="M2 6h12M2 10h12M4 4l-2 2 2 2M12 8l2 2-2 2"/></svg><span class="metric-label">Today's Range</span><span class="metric-value">71.2%</span></div>
      <div class="metric"><svg class="ico" viewBox="0 0 16 16"><path d="M2 2v12h12M4 5l3 4 3-2 3 5"/></svg><span class="metric-label">Current Debt</span><span class="metric-value"><sup>$</sup>16.68B</span></div>
      <div class="metric"><svg class="ico" viewBox="0 0 16 16"><path d="M1 9l7-4 7 4-7 4z M1 11l7 4 7-4"/></svg><span class="metric-label">Cash</span><span class="metric-value"><sup>$</sup>40.72B</span></div>
      <div class="metric"><svg class="ico" viewBox="0 0 16 16"><circle cx="8" cy="8" r="6"/><path d="M5 8h6M8 5v6"/></svg><span class="metric-label">Smart Stop</span><span class="metric-value"><sup>$</sup>4.35</span></div>
      <div class="metric"><svg class="ico" viewBox="0 0 16 16"><path d="M2 4h3l6 8h3M2 12h3l6-8h3"/></svg><span class="metric-label">Change Since Jan 1st</span><span class="metric-value is-down">-47.4%</span></div>
      <div class="metric"><svg class="ico" viewBox="0 0 16 16"><rect x="2" y="2" width="12" height="12" rx="3"/><path d="M6 11V8M8 11V5M10 11V7"/></svg><span class="metric-label">Options Volume Today</span><span class="metric-value">163.7%</span></div>
      <div class="metric"><svg class="ico" viewBox="0 0 16 16"><circle cx="8" cy="8" r="6"/><path d="M8 2v6h6"/></svg><span class="metric-label">Market Cap</span><span class="metric-value">$475.69B</span></div>
      <div class="metric"><svg class="ico" viewBox="0 0 16 16"><path d="M2 9v-3M5 12V4M8 14V2M11 11V5M14 9V7"/></svg><span class="metric-label">Short Float</span><span class="metric-value">1.07%</span></div>
      <div class="metric"><svg class="ico" viewBox="0 0 16 16"><rect x="2" y="3" width="12" height="11" rx="1"/><path d="M2 6h12M6 10l2 2 3-4"/></svg><span class="metric-label">Volume Today</span><span class="metric-value"><span class="tri">▲</span>55.8</span></div>
      <div class="metric"><svg class="ico" viewBox="0 0 16 16"><circle cx="6" cy="8" r="4.5"/><circle cx="10" cy="8" r="4.5"/></svg><span class="metric-label">Days to Cover</span><span class="metric-value">0.72</span></div>
      <div class="metric"><svg class="ico" viewBox="0 0 16 16"><rect x="1.5" y="4" width="13" height="8" rx="1"/><circle cx="8" cy="8" r="2"/></svg><span class="metric-label">Revenue</span><span class="metric-value"><sup>$</sup>119.41B</span></div>
    </div>
    <nav class="nav">
      <span class="nav-item is-active"><svg viewBox="0 0 12 12"><rect x="1" y="1.5" width="10" height="9" rx="1"/><path d="M3 4h3M3 6h6M3 8h6"/></svg>Details</span>
      <span class="nav-item"><svg viewBox="0 0 12 12"><rect x="1" y="1.5" width="9" height="9" rx="1"/><path d="M3 4h5M3 6h5M3 8h3M10 4h1v6.5"/></svg>News</span>
      <span class="nav-item"><svg viewBox="0 0 12 12"><rect x="2" y="1" width="8" height="10" rx="1"/><circle cx="6" cy="5" r="1.6"/><path d="M3.5 9c.5-1.5 4.5-1.5 5 0"/></svg>Profile</span>
      <span class="nav-item"><svg viewBox="0 0 12 12"><rect x="1" y="1.5" width="10" height="2.5"/><rect x="1" y="5" width="10" height="2.5"/><path d="M1 9.5h10"/></svg>Similar</span>
    </nav>
  </section>

  <!-- LIGHT: NEWS -->
  <section class="screen theme-light" style="left:488px;top:135px;height:693px">
    <div class="status"><span>11.58 am</span><span class="status-icons"><span class="sig"></span><span class="wifi"></span><span class="batt"></span></span></div>
    <div class="title" style="padding-bottom:18px">News</div>
    <div class="content">
      <div class="news-list">
        <article class="news-item"><div class="news-date"><svg class="ico" viewBox="0 0 16 16"><rect x="2" y="3" width="12" height="11" rx="1"/><path d="M2 6h12M5 1.5v3M11 1.5v3"/></svg>2.53 PM 08/11/2022</div><p class="news-headline">Social media giant Nova carries out 'Digital Massacre' of Palestinian posts</p><p class="news-source">- Harbor Desk</p></article>
        <article class="news-item"><div class="news-date"><svg class="ico" viewBox="0 0 16 16"><rect x="2" y="3" width="12" height="11" rx="1"/><path d="M2 6h12M5 1.5v3M11 1.5v3"/></svg>2.53 PM 8/11/2022</div><p class="news-headline">Nova says it is testing end - to -end encryption on backs, Chatline (NXE : NOVA)</p><p class="news-source">- Ledger Point</p></article>
        <article class="news-item"><div class="news-date"><svg class="ico" viewBox="0 0 16 16"><rect x="2" y="3" width="12" height="11" rx="1"/><path d="M2 6h12M5 1.5v3M11 1.5v3"/></svg>2.53 PM 8/11/2022</div><p class="news-headline">Shares of Nova Platforms Jumped After the Loop - parent said it had raised $10 Billion</p><p class="news-source">- The Civic Law Journal</p></article>
        <article class="news-item"><div class="news-date"><svg class="ico" viewBox="0 0 16 16"><rect x="2" y="3" width="12" height="11" rx="1"/><path d="M2 6h12M5 1.5v3M11 1.5v3"/></svg>2.53 PM 8/11/2022</div><p class="news-headline">Investing in Nova Platforms is a No - Brainer (NXE : NOVA)</p><p class="news-source">- Ledger Point</p></article>
        <article class="news-item"><div class="news-date"><svg class="ico" viewBox="0 0 16 16"><rect x="2" y="3" width="12" height="11" rx="1"/><path d="M2 6h12M5 1.5v3M11 1.5v3"/></svg>2.53 PM 8/11/2022</div><p class="news-headline">Navigation Labor Law in the Virtual World</p><p class="news-source">- Wireline</p></article>
      </div>
    </div>
    <nav class="nav">
      <span class="nav-item"><svg viewBox="0 0 12 12"><rect x="1" y="1.5" width="10" height="9" rx="1"/><path d="M3 4h3M3 6h6M3 8h6"/></svg>Details</span>
      <span class="nav-item is-active"><svg viewBox="0 0 12 12"><rect x="1" y="1.5" width="9" height="9" rx="1"/><path d="M3 4h5M3 6h5M3 8h3M10 4h1v6.5"/></svg>News</span>
      <span class="nav-item"><svg viewBox="0 0 12 12"><rect x="2" y="1" width="8" height="10" rx="1"/><circle cx="6" cy="5" r="1.6"/><path d="M3.5 9c.5-1.5 4.5-1.5 5 0"/></svg>Profile</span>
      <span class="nav-item"><svg viewBox="0 0 12 12"><rect x="1" y="1.5" width="10" height="2.5"/><rect x="1" y="5" width="10" height="2.5"/><path d="M1 9.5h10"/></svg>Similar</span>
    </nav>
  </section>

  <!-- LIGHT: PROFILE -->
  <section class="screen theme-light" style="left:811px;top:135px;height:909px">
    <div class="status"><span>11.58 am</span><span class="status-icons"><span class="sig"></span><span class="wifi"></span><span class="batt"></span></span></div>
    <div class="title" style="padding-bottom:23px">Profile</div>
    <div class="content">
      <div class="profile-body">
        <div class="profile-card"><div class="profile-card-head"><svg class="ico" viewBox="0 0 22 22"><rect x="2" y="2" width="16" height="16"/><path d="M5 15V9l4 3V8l4 3v4zM14 6h2"/></svg>Sector</div><p>Professional, Scientific &amp; Technical Services</p></div>
        <div class="profile-card"><div class="profile-card-head"><svg class="ico" viewBox="0 0 22 22"><rect x="2" y="3" width="13" height="16"/><path d="M5 7h7M5 10h7M5 13h4M13 17l6-6 2 2-6 6h-2z"/></svg>Sub Sector</div><p>Professional, Scientific and Technical Services</p></div>
        <div class="profile-card"><div class="profile-card-head"><svg class="ico" viewBox="0 0 22 22"><rect x="2" y="5" width="15" height="11"/><path d="M7 19h6M10 16v3M5 9h6M5 12h8"/><circle cx="17" cy="5" r="3"/></svg>Industry Group</div><p>Computer Systems Design and Related Services</p></div>
        <div class="profile-card"><div class="profile-card-head"><svg class="ico" viewBox="0 0 22 22"><rect x="2" y="5" width="15" height="11"/><path d="M7 19h6M10 16v3"/><circle cx="9" cy="10" r="2.5"/><circle cx="17" cy="5" r="3"/></svg>Industry</div><p>Computer Systems Design and Related Services</p></div>
        <div class="profile-card"><div class="profile-card-head"><svg class="ico" viewBox="0 0 22 22"><rect x="2" y="3" width="16" height="13"/><path d="M2 7h16M5 10h4M5 13h6"/><circle cx="16" cy="16" r="3"/></svg>Sub Industry</div><p>Custom Computer Programming Services</p></div>
        <h3 class="section-label">BUSINESS SUMMARY</h3>
        <div class="summary">Lorem ipsum dolor sit amet, consectetur adipiscing elit, sed do eiusmod tempor incididunt ut labore et dolore magna aliqua. Ut enim ad minim veniam, quis nostrud exercitation ullamco laboris nisi ut aliquip ex ea commodo sequatquis nostrud exercitation ullamco laboris nisi ut aliquip ex ea commodo consequat</div>
      </div>
    </div>
    <nav class="nav">
      <span class="nav-item"><svg viewBox="0 0 12 12"><rect x="1" y="1.5" width="10" height="9" rx="1"/><path d="M3 4h3M3 6h6M3 8h6"/></svg>Details</span>
      <span class="nav-item"><svg viewBox="0 0 12 12"><rect x="1" y="1.5" width="9" height="9" rx="1"/><path d="M3 4h5M3 6h5M3 8h3M10 4h1v6.5"/></svg>News</span>
      <span class="nav-item is-active"><svg viewBox="0 0 12 12"><rect x="2" y="1" width="8" height="10" rx="1"/><circle cx="6" cy="5" r="1.6"/><path d="M3.5 9c.5-1.5 4.5-1.5 5 0"/></svg>Profile</span>
      <span class="nav-item"><svg viewBox="0 0 12 12"><rect x="1" y="1.5" width="10" height="2.5"/><rect x="1" y="5" width="10" height="2.5"/><path d="M1 9.5h10"/></svg>Similar</span>
    </nav>
  </section>

  <!-- LIGHT: SIMILAR -->
  <section class="screen theme-light" style="left:1133px;top:140px;height:909px">
    <div class="status"><span>11.58 am</span><span class="status-icons"><span class="sig"></span><span class="wifi"></span><span class="batt"></span></span></div>
    <div class="title" style="padding-bottom:23px">Similar to NOVA</div>
    <div class="content">
      <div class="select-label">Select Symbol</div>
      <div class="search"><svg viewBox="0 0 10 10"><circle cx="4" cy="4" r="3"/><path d="M6.3 6.3 9 9"/></svg>Search by symbol</div>
      <div class="symbol-panel">
        <div class="symbol-row">BQWX <svg class="chev" viewBox="0 0 8 5"><path d="M.5.5 4 4 7.5.5"/></svg></div>
        <div class="stat">Price<strong>2.28B</strong></div>
        <div class="stat">Chg Close (%)<strong>2.28B</strong></div>
        <div class="stat">Relative Volume (Ratio)<strong>141.74</strong></div>
        <div class="stat">Volume Today (Shares)<strong>4.089.884</strong></div>
        <div class="company-name">Company Name<strong>BlueRidge Technology SLTN</strong></div>
      </div>
      <div class="symbol-row">QXIV <svg class="chev" viewBox="0 0 8 5"><path d="M.5.5 4 4 7.5.5"/></svg></div>
      <div class="symbol-row">ZQ <svg class="chev" viewBox="0 0 8 5"><path d="M.5.5 4 4 7.5.5"/></svg></div>
      <div class="symbol-row">VLMQ <svg class="chev" viewBox="0 0 8 5"><path d="M.5.5 4 4 7.5.5"/></svg></div>
      <div class="symbol-row">XPQ <svg class="chev" viewBox="0 0 8 5"><path d="M.5.5 4 4 7.5.5"/></svg></div>
      <div class="symbol-row">QOZO <svg class="chev" viewBox="0 0 8 5"><path d="M.5.5 4 4 7.5.5"/></svg></div>
      <div class="symbol-row">ZAVQ <svg class="chev" viewBox="0 0 8 5"><path d="M.5.5 4 4 7.5.5"/></svg></div>
      <div class="symbol-row">KQYX <svg class="chev" viewBox="0 0 8 5"><path d="M.5.5 4 4 7.5.5"/></svg></div>
      <div class="symbol-row">TXQZ <svg class="chev" viewBox="0 0 8 5"><path d="M.5.5 4 4 7.5.5"/></svg></div>
      <div class="symbol-row">ZMQR <svg class="chev" viewBox="0 0 8 5"><path d="M.5.5 4 4 7.5.5"/></svg></div>
      <div class="symbol-row">QMXL <svg class="chev" viewBox="0 0 8 5"><path d="M.5.5 4 4 7.5.5"/></svg></div>
    </div>
    <nav class="nav">
      <span class="nav-item"><svg viewBox="0 0 12 12"><rect x="1" y="1.5" width="10" height="9" rx="1"/><path d="M3 4h3M3 6h6M3 8h6"/></svg>Details</span>
      <span class="nav-item"><svg viewBox="0 0 12 12"><rect x="1" y="1.5" width="9" height="9" rx="1"/><path d="M3 4h5M3 6h5M3 8h3M10 4h1v6.5"/></svg>News</span>
      <span class="nav-item"><svg viewBox="0 0 12 12"><rect x="2" y="1" width="8" height="10" rx="1"/><circle cx="6" cy="5" r="1.6"/><path d="M3.5 9c.5-1.5 4.5-1.5 5 0"/></svg>Profile</span>
      <span class="nav-item is-active"><svg viewBox="0 0 12 12"><rect x="1" y="1.5" width="10" height="2.5"/><rect x="1" y="5" width="10" height="2.5"/><path d="M1 9.5h10"/></svg>Similar</span>
    </nav>
  </section>

  <!-- DARK: DETAILS -->
  <section class="screen theme-dark" style="left:160px;top:1250px;height:909px">
    <div class="status"><span>11.58 am</span><span class="status-icons"><span class="sig"></span><span class="wifi"></span><span class="batt"></span></span></div>
    <div class="title">Details</div>
    <div class="picker">NOVA <svg class="chev" viewBox="0 0 8 5"><path d="M.5.5 4 4 7.5.5"/></svg></div>
    <div class="company"><span class="company-mark"></span>Nova Platforms, Inc. (NXE:NOVA)</div>
    <div class="content">
      <div class="quote">
        <div class="brand-word">NOVA</div>
        <div>
          <div class="price">176.99</div>
          <div class="quote-time" style="color:#fff"><svg class="ico" viewBox="0 0 16 16"><rect x="2" y="3" width="12" height="11" rx="1"/><path d="M2 6h12M5 1.5v3M11 1.5v3"/></svg>2.53 PM 8/11/2022</div>
          <div class="change">-1.35 (-0.76%)</div>
        </div>
      </div>
      <div class="volume-box">
        <div class="volume-col">Volume<strong>19,012,888</strong></div>
        <div class="volume-col">Relative Volume<strong>0.92</strong></div>
      </div>
      <div class="metric"><svg class="ico" viewBox="0 0 16 16"><path d="M2 9v-3M5 12V4M8 14V2M11 11V5M14 9V7"/></svg><span class="metric-label">Float</span><span class="metric-value">2.28B</span></div>
      <div class="metric"><svg class="ico" viewBox="0 0 16 16"><rect x="2" y="3" width="12" height="11" rx="1"/><path d="M2 6h12M5 1.5v3M11 1.5v3"/><circle cx="11" cy="11" r="2.5"/></svg><span class="metric-label">Earnings Date</span><span class="metric-value">July 27<small>POST.MKT</small></span></div>
      <div class="metric"><svg class="ico" viewBox="0 0 16 16"><path d="M2 6h12M2 10h12M4 4l-2 2 2 2M12 8l2 2-2 2"/></svg><span class="metric-label">Today's Range</span><span class="metric-value">71.2%</span></div>
      <div class="metric"><svg class="ico" viewBox="0 0 16 16"><path d="M2 2v12h12M4 5l3 4 3-2 3 5"/></svg><span class="metric-label">Current Debt</span><span class="metric-value"><sup>$</sup>16.68B</span></div>
      <div class="metric"><svg class="ico" viewBox="0 0 16 16"><path d="M1 9l7-4 7 4-7 4z M1 11l7 4 7-4"/></svg><span class="metric-label">Cash</span><span class="metric-value"><sup>$</sup>40.72B</span></div>
      <div class="metric"><svg class="ico" viewBox="0 0 16 16"><circle cx="8" cy="8" r="6"/><path d="M5 8h6M8 5v6"/></svg><span class="metric-label">Smart Stop</span><span class="metric-value"><sup>$</sup>4.35</span></div>
      <div class="metric"><svg class="ico" viewBox="0 0 16 16"><path d="M2 4h3l6 8h3M2 12h3l6-8h3"/></svg><span class="metric-label">Change Since Jan 1st</span><span class="metric-value is-down">-47.4%</span></div>
      <div class="metric"><svg class="ico" viewBox="0 0 16 16"><rect x="2" y="2" width="12" height="12" rx="3"/><path d="M6 11V8M8 11V5M10 11V7"/></svg><span class="metric-label">Options Volume Today</span><span class="metric-value">163.7%</span></div>
      <div class="metric"><svg class="ico" viewBox="0 0 16 16"><circle cx="8" cy="8" r="6"/><path d="M8 2v6h6"/></svg><span class="metric-label">Market Cap</span><span class="metric-value">$475.69B</span></div>
      <div class="metric"><svg class="ico" viewBox="0 0 16 16"><path d="M2 9v-3M5 12V4M8 14V2M11 11V5M14 9V7"/></svg><span class="metric-label">Short Float</span><span class="metric-value">1.07%</span></div>
      <div class="metric"><svg class="ico" viewBox="0 0 16 16"><rect x="2" y="3" width="12" height="11" rx="1"/><path d="M2 6h12M6 10l2 2 3-4"/></svg><span class="metric-label">Volume Today</span><span class="metric-value"><span class="tri">▲</span>55.8</span></div>
      <div class="metric"><svg class="ico" viewBox="0 0 16 16"><circle cx="6" cy="8" r="4.5"/><circle cx="10" cy="8" r="4.5"/></svg><span class="metric-label">Days to Cover</span><span class="metric-value">0.72</span></div>
      <div class="metric"><svg class="ico" viewBox="0 0 16 16"><rect x="1.5" y="4" width="13" height="8" rx="1"/><circle cx="8" cy="8" r="2"/></svg><span class="metric-label">Revenue</span><span class="metric-value"><sup>$</sup>119.41B</span></div>
    </div>
    <nav class="nav">
      <span class="nav-item is-active"><svg viewBox="0 0 12 12"><rect x="1" y="1.5" width="10" height="9" rx="1"/><path d="M3 4h3M3 6h6M3 8h6"/></svg>Details</span>
      <span class="nav-item"><svg viewBox="0 0 12 12"><rect x="1" y="1.5" width="9" height="9" rx="1"/><path d="M3 4h5M3 6h5M3 8h3M10 4h1v6.5"/></svg>News</span>
      <span class="nav-item"><svg viewBox="0 0 12 12"><rect x="2" y="1" width="8" height="10" rx="1"/><circle cx="6" cy="5" r="1.6"/><path d="M3.5 9c.5-1.5 4.5-1.5 5 0"/></svg>Profile</span>
      <span class="nav-item"><svg viewBox="0 0 12 12"><rect x="1" y="1.5" width="10" height="2.5"/><rect x="1" y="5" width="10" height="2.5"/><path d="M1 9.5h10"/></svg>Similar</span>
    </nav>
  </section>

  <!-- DARK: NEWS -->
  <section class="screen theme-dark" style="left:488px;top:1254px;height:693px">
    <div class="status"><span>11.58 am</span><span class="status-icons"><span class="sig"></span><span class="wifi"></span><span class="batt"></span></span></div>
    <div class="title" style="padding-bottom:18px">News</div>
    <div class="content">
      <div class="news-list">
        <article class="news-item"><div class="news-date"><svg class="ico" viewBox="0 0 16 16"><rect x="2" y="3" width="12" height="11" rx="1"/><path d="M2 6h12M5 1.5v3M11 1.5v3"/></svg>2.53 PM 08/11/2022</div><p class="news-headline">Social media giant Nova carries out 'Digital Massacre' of Palestinian posts</p><p class="news-source">- Harbor Desk</p></article>
        <article class="news-item"><div class="news-date"><svg class="ico" viewBox="0 0 16 16"><rect x="2" y="3" width="12" height="11" rx="1"/><path d="M2 6h12M5 1.5v3M11 1.5v3"/></svg>2.53 PM 8/11/2022</div><p class="news-headline">Nova says it is testing end - to -end encryption on backs, Chatline (NXE : NOVA)</p><p class="news-source">- Ledger Point</p></article>
        <article class="news-item"><div class="news-date"><svg class="ico" viewBox="0 0 16 16"><rect x="2" y="3" width="12" height="11" rx="1"/><path d="M2 6h12M5 1.5v3M11 1.5v3"/></svg>2.53 PM 8/11/2022</div><p class="news-headline">Shares of Nova Platforms Jumped After the Loop - parent said it had raised $10 Billion</p><p class="news-source">- The Civic Law Journal</p></article>
        <article class="news-item"><div class="news-date"><svg class="ico" viewBox="0 0 16 16"><rect x="2" y="3" width="12" height="11" rx="1"/><path d="M2 6h12M5 1.5v3M11 1.5v3"/></svg>2.53 PM 8/11/2022</div><p class="news-headline">Investing in Nova Platforms is a No - Brainer (NXE : NOVA)</p><p class="news-source">- Ledger Point</p></article>
        <article class="news-item"><div class="news-date"><svg class="ico" viewBox="0 0 16 16"><rect x="2" y="3" width="12" height="11" rx="1"/><path d="M2 6h12M5 1.5v3M11 1.5v3"/></svg>2.53 PM 8/11/2022</div><p class="news-headline">Navigation Labor Law in the Virtual World</p><p class="news-source">- Wireline</p></article>
      </div>
    </div>
    <nav class="nav">
      <span class="nav-item"><svg viewBox="0 0 12 12"><rect x="1" y="1.5" width="10" height="9" rx="1"/><path d="M3 4h3M3 6h6M3 8h6"/></svg>Details</span>
      <span class="nav-item is-active"><svg viewBox="0 0 12 12"><rect x="1" y="1.5" width="9" height="9" rx="1"/><path d="M3 4h5M3 6h5M3 8h3M10 4h1v6.5"/></svg>News</span>
      <span class="nav-item"><svg viewBox="0 0 12 12"><rect x="2" y="1" width="8" height="10" rx="1"/><circle cx="6" cy="5" r="1.6"/><path d="M3.5 9c.5-1.5 4.5-1.5 5 0"/></svg>Profile</span>
      <span class="nav-item"><svg viewBox="0 0 12 12"><rect x="1" y="1.5" width="10" height="2.5"/><rect x="1" y="5" width="10" height="2.5"/><path d="M1 9.5h10"/></svg>Similar</span>
    </nav>
  </section>

  <!-- DARK: PROFILE -->
  <section class="screen theme-dark" style="left:811px;top:1257px;height:909px">
    <div class="status"><span>11.58 am</span><span class="status-icons"><span class="sig"></span><span class="wifi"></span><span class="batt"></span></span></div>
    <div class="title" style="padding-bottom:23px">Profile</div>
    <div class="content">
      <div class="profile-body">
        <div class="profile-card"><div class="profile-card-head"><svg class="ico" viewBox="0 0 22 22"><rect x="2" y="2" width="16" height="16"/><path d="M5 15V9l4 3V8l4 3v4zM14 6h2"/></svg>Sector</div><p>Professional, Scientific &amp; Technical Services</p></div>
        <div class="profile-card"><div class="profile-card-head"><svg class="ico" viewBox="0 0 22 22"><rect x="2" y="3" width="13" height="16"/><path d="M5 7h7M5 10h7M5 13h4M13 17l6-6 2 2-6 6h-2z"/></svg>Sub Sector</div><p>Professional, Scientific and Technical Services</p></div>
        <div class="profile-card"><div class="profile-card-head"><svg class="ico" viewBox="0 0 22 22"><rect x="2" y="5" width="15" height="11"/><path d="M7 19h6M10 16v3M5 9h6M5 12h8"/><circle cx="17" cy="5" r="3"/></svg>Industry Group</div><p>Computer Systems Design and Related Services</p></div>
        <div class="profile-card"><div class="profile-card-head"><svg class="ico" viewBox="0 0 22 22"><rect x="2" y="5" width="15" height="11"/><path d="M7 19h6M10 16v3"/><circle cx="9" cy="10" r="2.5"/><circle cx="17" cy="5" r="3"/></svg>Industry</div><p>Computer Systems Design and Related Services</p></div>
        <div class="profile-card"><div class="profile-card-head"><svg class="ico" viewBox="0 0 22 22"><rect x="2" y="3" width="16" height="13"/><path d="M2 7h16M5 10h4M5 13h6"/><circle cx="16" cy="16" r="3"/></svg>Sub Industry</div><p>Custom Computer Programming Services</p></div>
        <h3 class="section-label">BUSINESS SUMMARY</h3>
        <div class="summary">Lorem ipsum dolor sit amet, consectetur adipiscing elit, sed do eiusmod tempor incididunt ut labore et dolore magna aliqua. Ut enim ad minim veniam, quis nostrud exercitation ullamco laboris nisi ut aliquip ex ea commodo sequatquis nostrud exercitation ullamco laboris nisi ut aliquip ex ea commodo consequat</div>
      </div>
    </div>
    <nav class="nav">
      <span class="nav-item"><svg viewBox="0 0 12 12"><rect x="1" y="1.5" width="10" height="9" rx="1"/><path d="M3 4h3M3 6h6M3 8h6"/></svg>Details</span>
      <span class="nav-item"><svg viewBox="0 0 12 12"><rect x="1" y="1.5" width="9" height="9" rx="1"/><path d="M3 4h5M3 6h5M3 8h3M10 4h1v6.5"/></svg>News</span>
      <span class="nav-item is-active"><svg viewBox="0 0 12 12"><rect x="2" y="1" width="8" height="10" rx="1"/><circle cx="6" cy="5" r="1.6"/><path d="M3.5 9c.5-1.5 4.5-1.5 5 0"/></svg>Profile</span>
      <span class="nav-item"><svg viewBox="0 0 12 12"><rect x="1" y="1.5" width="10" height="2.5"/><rect x="1" y="5" width="10" height="2.5"/><path d="M1 9.5h10"/></svg>Similar</span>
    </nav>
  </section>

  <!-- DARK: SIMILAR -->
  <section class="screen theme-dark" style="left:1133px;top:1260px;height:909px">
    <div class="status"><span>11.58 am</span><span class="status-icons"><span class="sig"></span><span class="wifi"></span><span class="batt"></span></span></div>
    <div class="title" style="padding-bottom:23px">Similar to NOVA</div>
    <div class="content">
      <div class="select-label">Select Symbol</div>
      <div class="search"><svg viewBox="0 0 10 10"><circle cx="4" cy="4" r="3"/><path d="M6.3 6.3 9 9"/></svg>Search by symbol</div>
      <div class="symbol-panel">
        <div class="symbol-row">BQWX <svg class="chev" viewBox="0 0 8 5"><path d="M.5.5 4 4 7.5.5"/></svg></div>
        <div class="stat">Price<strong>2.28B</strong></div>
        <div class="stat">Chg Close (%)<strong>2.28B</strong></div>
        <div class="stat">Relative Volume (Ratio)<strong>141.74</strong></div>
        <div class="stat">Volume Today (Shares)<strong>4.089.884</strong></div>
        <div class="company-name">Company Name<strong>BlueRidge Technology SLTN</strong></div>
      </div>
      <div class="symbol-row">QXIV <svg class="chev" viewBox="0 0 8 5"><path d="M.5.5 4 4 7.5.5"/></svg></div>
      <div class="symbol-row">ZQ <svg class="chev" viewBox="0 0 8 5"><path d="M.5.5 4 4 7.5.5"/></svg></div>
      <div class="symbol-row">VLMQ <svg class="chev" viewBox="0 0 8 5"><path d="M.5.5 4 4 7.5.5"/></svg></div>
      <div class="symbol-row">XPQ <svg class="chev" viewBox="0 0 8 5"><path d="M.5.5 4 4 7.5.5"/></svg></div>
      <div class="symbol-row">QOZO <svg class="chev" viewBox="0 0 8 5"><path d="M.5.5 4 4 7.5.5"/></svg></div>
      <div class="symbol-row">ZAVQ <svg class="chev" viewBox="0 0 8 5"><path d="M.5.5 4 4 7.5.5"/></svg></div>
      <div class="symbol-row">KQYX <svg class="chev" viewBox="0 0 8 5"><path d="M.5.5 4 4 7.5.5"/></svg></div>
      <div class="symbol-row">TXQZ <svg class="chev" viewBox="0 0 8 5"><path d="M.5.5 4 4 7.5.5"/></svg></div>
      <div class="symbol-row">ZMQR <svg class="chev" viewBox="0 0 8 5"><path d="M.5.5 4 4 7.5.5"/></svg></div>
      <div class="symbol-row">QMXL <svg class="chev" viewBox="0 0 8 5"><path d="M.5.5 4 4 7.5.5"/></svg></div>
    </div>
    <nav class="nav">
      <span class="nav-item"><svg viewBox="0 0 12 12"><rect x="1" y="1.5" width="10" height="9" rx="1"/><path d="M3 4h3M3 6h6M3 8h6"/></svg>Details</span>
      <span class="nav-item"><svg viewBox="0 0 12 12"><rect x="1" y="1.5" width="9" height="9" rx="1"/><path d="M3 4h5M3 6h5M3 8h3M10 4h1v6.5"/></svg>News</span>
      <span class="nav-item"><svg viewBox="0 0 12 12"><rect x="2" y="1" width="8" height="10" rx="1"/><circle cx="6" cy="5" r="1.6"/><path d="M3.5 9c.5-1.5 4.5-1.5 5 0"/></svg>Profile</span>
      <span class="nav-item is-active"><svg viewBox="0 0 12 12"><rect x="1" y="1.5" width="10" height="2.5"/><rect x="1" y="5" width="10" height="2.5"/><path d="M1 9.5h10"/></svg>Similar</span>
    </nav>
  </section>

</div>
</body>
</html>
```